Plumweave Inc. Website & Korvix Apps Landing Pages

We need a web site design for our company. We develop software and do various consultant projects for our clients. Our products focus on the mobile platform, mainly the Korvix (business, games, social, etc.). We want to communicate that our software is simple and good as candy. The web pages should be fun to look at not loosing seriousness and credibility. Web 2.0 style and 960 grid system a must. We are opened to any overall site colour scheme suggestions (look at the sites we like below).

Must haves:
- Our logo should be seen on the site and look great on it :-) (preview attached below)
- Main home page and app landing page.
- Section links/tabs on the home page (home,apps,support,blog,contact,about)
- No text in images
- Style sheet

Looks we like:
- http://x7k3lmq9pwrtzv.pixelmoorvault.net/412_Zelto_Site/final_large.jpg
- http://x7k3lmq9pwrtzv.pixelmoorvault.net/Premium_71_Illustrative_Korvix_Landing_Page/final.jpg
- http://grelmwick.com/
- http://dorniply.ca/
- http://quatzel.com/

Industry/Entity Type

Business

Requirements
Must have
• - Company logo should look great on pages.
• - Main home page and app landing page.
• - Section links/tabs on the home page (home,apps,support,blog,contact,about)
• - Web 2.0 style.
• - 960 grid system (12 col, 16 col).
• - Sliced ann optmized
• - Exported in all major formats (psd,ai,eps,png,jpeg,etc)
• - Style sheet
Should not have
• - Text in images

```html
<!DOCTYPE html>
<html lang="en">
<head>
<meta charset="utf-8">
<title>Plumweave — Korvix Apps</title>
<link href="https://fonts.googleapis.com/css2?family=Arimo:wght@400;700&family=Questrial&display=swap" rel="stylesheet">
<style>
:root{
  --page-dark:#2e2d2d;
  --page-darker:#1f1e1e;
  --panel:#ffffff;
  --brand-red:#d9322e;
  --heading-red:#e2473f;
  --text:#4a4a4a;
  --text-dark:#1e1e1e;
  --footer-text:#e2e2e2;
  --orange:#f7941d;
}
*{margin:0;padding:0;box-sizing:border-box}
html,body{width:830px;height:1200px;overflow:hidden}
body{
  position:relative;
  background:linear-gradient(#2a2929 0,var(--page-dark) 300px,var(--page-dark) 1104px,var(--page-darker) 1104px);
  font-family:"Arimo",Arial,sans-serif;color:var(--text);
}
.panel{position:absolute;left:28px;top:27px;width:777px;height:824px;background:var(--panel);border-radius:7px}
.brand{position:absolute;left:25px;top:24px;font-family:"Questrial",sans-serif;font-size:34px;color:var(--brand-red);display:flex;align-items:center;gap:8px}
.brand-dot{width:14px;height:14px;border-radius:50%;background:var(--brand-red)}
.main-nav{position:absolute;top:14px;right:34px;display:flex}
.main-nav a{display:flex;flex-direction:column;align-items:center;text-decoration:none;color:#555;font-size:15px;padding:0 9px}
.main-nav svg{width:26px;height:26px;margin-bottom:12px}
.main-nav a.current{color:var(--brand-red)}
.main-nav a.current span{border-bottom:2px solid var(--brand-red);padding-bottom:2px}
.hero{position:absolute;left:22px;top:85px;width:731px;height:363px;border-radius:6px;
  background:radial-gradient(ellipse at 55% 45%,#ffffff 0,#eef3f7 55%,#d9e6ef 100%);
  box-shadow:0 14px 12px -10px rgba(0,0,0,.25);overflow:hidden}
.hero-art{position:absolute;inset:0;
  background:linear-gradient(120deg,rgba(240,60,120,.55) 0,rgba(250,180,40,.5) 14%,rgba(120,200,60,.35) 24%,transparent 32%),
  linear-gradient(90deg,transparent 26%,#1a1a1a 26%,#2b2b2b 52%,#3a2a24 62%,#1d1d1d 72%,transparent 73%);
  opacity:.9}
.download-btn{position:absolute;left:501px;top:286px;width:215px;height:55px;border-radius:12px;
  background:linear-gradient(#ffcf6a,var(--orange) 55%,#f08a10);border:2px solid #fff3d4;
  box-shadow:0 2px 4px rgba(0,0,0,.25);display:flex;align-items:center;justify-content:center;gap:4px;
  font-weight:700;font-size:22px;color:#1d1d1d;letter-spacing:-.6px;white-space:nowrap;text-decoration:none}
.download-btn svg{width:20px;height:32px;margin-top:-16px;flex:none}
.col-rule{position:absolute;top:491px;width:1px;height:292px;background:#e8e8e8}
.col-head{position:absolute;display:flex;align-items:center;gap:6px;font-size:21px;font-weight:400;line-height:34px;color:var(--heading-red);letter-spacing:-.3px;white-space:nowrap}
.col-head svg{width:34px;height:34px;flex:none}
.features{position:absolute;left:22px;top:545px;width:230px;list-style:none}
.features li{position:relative;padding-left:22px;font-size:10.5px;line-height:13.8px;color:var(--text);margin-bottom:13px;white-space:nowrap;letter-spacing:.15px}
.features li svg{position:absolute;left:0;top:0;width:16px;height:16px}
.demo{position:absolute;left:241px;top:549px;width:275px;height:194px;background:linear-gradient(#2a2a2a,#000 85%)}
.demo-play{position:absolute;left:98px;top:74px;width:79px;height:24px;border-radius:12px;background:linear-gradient(#6a6a6a,#3b3b3b);
  border:1px solid #999;color:#ddd;font-size:8.5px;display:flex;align-items:center;padding-left:13px}
.demo-play i{position:absolute;right:0;top:-1px;width:24px;height:24px;border-radius:50%;border:1px solid #bbb;background:#444}
.demo-play i:after{content:"";position:absolute;left:8px;top:6px;border-left:8px solid #ddd;border-top:5px solid transparent;border-bottom:5px solid transparent}
.demo-bar{position:absolute;left:0;bottom:0;width:100%;height:16px;background:linear-gradient(#33414a,#1a2228);display:flex;align-items:center;padding:0 5px;gap:5px}
.demo-track{flex:1;height:5px;background:#0d0d0d;border-radius:3px}
.demo-time{font-size:7px;color:#5bb4e0}
.demo-time b{color:#ddd;font-weight:400}
.testimonial{position:absolute;left:548px;top:546px;width:215px;font-size:10.5px;line-height:19.5px;color:var(--text);white-space:nowrap;letter-spacing:.15px}
.testimonial cite{display:block;font-style:normal;font-weight:700;color:var(--text-dark)}
.footer-col{position:absolute;top:876px;color:var(--footer-text)}
.footer-col h2{font-size:16px;font-weight:700;color:#e8e8e8;text-shadow:0 1px 2px #000;letter-spacing:-.3px;padding-bottom:5px;border-bottom:1px solid #555;margin-bottom:12px}
.footer-col p{font-size:11px;line-height:13.7px}
.blog-entry{margin-bottom:13px}
.bottom-bar{position:absolute;left:0;top:1104px;width:830px;height:96px;border-top:1px solid #3a3a3a}
.bottom-nav{position:absolute;left:38px;top:19px;font-size:11px;font-weight:700;color:#fff}
.bottom-nav a{color:#fff;text-decoration:none}
.bottom-nav span{margin:0 8px}
.bottom-brand{position:absolute;right:35px;top:9px;font-family:"Questrial",sans-serif;font-size:20px;color:#6e6e6e}
.copyright{position:absolute;right:35px;top:40px;font-size:9px;color:#6e6e6e}
</style>
</head>
<body>
<div class="panel">
  <div class="brand"><span class="brand-dot"></span>plumweave</div>
  <nav class="main-nav">
    <a href="#" class="current"><svg viewBox="0 0 26 26"><path d="M3 13 13 4l10 9h-3v9H6v-9z" fill="#4a8fc9"/><circle cx="13" cy="15" r="4" fill="#fff"/></svg><span>home</span></a>
    <a href="#"><svg viewBox="0 0 26 26"><g fill="#e03c8a"><circle cx="7" cy="7" r="3"/><circle cx="19" cy="19" r="3"/></g><g fill="#3b8fe0"><circle cx="19" cy="7" r="3"/><circle cx="7" cy="19" r="3"/></g><circle cx="13" cy="13" r="3" fill="#f2b000"/></svg><span>apps</span></a>
    <a href="#"><svg viewBox="0 0 26 26"><circle cx="13" cy="13" r="10" fill="none" stroke="#d9322e" stroke-width="4"/><text x="13" y="18" font-size="13" text-anchor="middle" fill="#333" font-family="Arimo" font-weight="700">?</text></svg><span>support</span></a>
    <a href="#"><svg viewBox="0 0 26 26"><rect x="3" y="3" width="20" height="20" rx="4" fill="#f28a1e"/><circle cx="8" cy="18" r="2" fill="#fff"/><path d="M7 12a7 7 0 0 1 7 7M7 7a12 12 0 0 1 12 12" stroke="#fff" stroke-width="2" fill="none"/></svg><span>blog</span></a>
    <a href="#"><svg viewBox="0 0 26 26"><path d="M3 10l10-6 10 6v12H3z" fill="#cfe0ee"/><path d="M3 10l10 7 10-7" stroke="#7ea7c6" fill="none"/></svg><span>contact</span></a>
    <a href="#"><svg viewBox="0 0 26 26"><circle cx="13" cy="8" r="5" fill="#5fb52c"/><path d="M3 24c0-7 4-10 10-10s10 3 10 10z" fill="#5fb52c"/></svg><span>about</span></a>
  </nav>

  <div class="hero">
    <div class="hero-art" role="img" aria-label="Three Korvix phones showing app screens over a burst of colourful confetti squares"></div>
    <a class="download-btn" href="#">DOWNLOAD NOW<svg viewBox="0 0 22 34"><path d="M7 0h8v20h7L11 34 0 20h7z" fill="#e8561c"/></svg></a>
  </div>

  <div class="col-rule" style="left:232px"></div>
  <div class="col-rule" style="left:527px"></div>

  <h2 class="col-head" style="left:22px;top:497px"><svg viewBox="0 0 34 34"><rect x="4" y="4" width="22" height="26" fill="#f4f6f9" stroke="#9aa7b5"/><path d="M8 11h14M8 16h14M8 21h10" stroke="#9aa7b5"/><path d="M30 4 14 24l-2 5 5-3L32 6z" fill="#3a6fb8"/></svg>Features</h2>
  <ul class="features">
    <li><svg viewBox="0 0 16 16"><path d="M1 9l4 5L15 1" stroke="#666" stroke-width="1.6" fill="none"/></svg>Lorem ipsum dolor sit amet, con-<br>sectetur adipiscing elit. Nam eget<br>magna non.</li>
    <li><svg viewBox="0 0 16 16"><path d="M1 9l4 5L15 1" stroke="#666" stroke-width="1.6" fill="none"/></svg>Lorem ipsum dolor sit amet, con-<br>sectetur adipiscing elit. Nam eget<br>magna non.</li>
    <li><svg viewBox="0 0 16 16"><path d="M1 9l4 5L15 1" stroke="#666" stroke-width="1.6" fill="none"/></svg>Lorem ipsum dolor sit amet, con-<br>sectetur adipiscing elit. Nam eget<br>magna non.</li>
    <li><svg viewBox="0 0 16 16"><path d="M1 9l4 5L15 1" stroke="#666" stroke-width="1.6" fill="none"/></svg>Lorem ipsum dolor sit amet, con-<br>sectetur adipiscing elit. Nam eget<br>magna non.</li>
  </ul>

  <h2 class="col-head" style="left:245px;top:500px"><svg viewBox="0 0 34 34"><rect x="2" y="6" width="16" height="11" fill="#3b8fe0"/><path d="M2 20h20M5 20v10M19 20v10" stroke="#3b8fe0" stroke-width="2.5"/><circle cx="27" cy="5" r="3.5" fill="#f28a1e"/><path d="M23 10h8v10h-2v10h-4V20h-2z" fill="#f28a1e"/></svg>Check out the DEMO</h2>
  <div class="demo">
    <div class="demo-play">Show me<i></i></div>
    <div class="demo-bar"><div class="demo-track"></div><span class="demo-time">00:27 / <b>02:04</b></span><div class="demo-track" style="flex:0 0 28px"></div></div>
  </div>

  <h2 class="col-head" style="left:545px;top:497px"><svg viewBox="0 0 34 34"><circle cx="10" cy="18" r="5" fill="#5fb52c"/><path d="M1 32c0-6 4-8 9-8s9 2 9 8z" fill="#5fb52c"/><ellipse cx="24" cy="9" rx="9" ry="7" fill="#e9f4fc" stroke="#5aa6dc"/></svg>Testimonials</h2>
  <blockquote class="testimonial">"We had been waiting for an easy to<br>use application like Plumweave that<br>would combine collaboration func-<br>tions (similar to those in popular<br>social networking sites), security that<br>would enable us to protect assets<br>and access, and robust file sharing<br>that was reliable and would accom-<br>modate the size and variety of files<br>we work with."
    <cite>Marta Quillen</cite><cite>CEO, Company</cite>
  </blockquote>
</div>

<section class="footer-col" style="left:38px;width:205px">
  <h2>About Plumweave</h2>
  <p>Lorem ipsum dolor sit amet, consectetur adipiscing elit. Nam eget magna non. Lorem ipsum dolor sit amet, consectetur adipiscing elit. Nam eget magna non. Lorem ipsum dolor sit amet, consectetur adipiscing elit.</p>
  <p style="margin-top:13px">Nam eget magna non.<br>Lorem ipsum dolor sit amet, consectetur adipiscing elit. Nam eget magna non.</p>
</section>
<section class="footer-col" style="left:280px;width:260px">
  <h2>Support</h2>
  <p>Lorem ipsum dolor sit amet, consectetur adipiscing elit. Nam eget magna non. Lorem ipsum dolor sit amet, consectetur adipiscing elit. Nam eget magna non. Lorem ipsum dolor sit amet, consectetur adip-iscing elit. Lorem ipsum dolor sit amet, consectetur adipiscing elit. Nam eget magna non. Lorem ipsum dolor sit amet, consectetur adipiscing elit. Nam eget magna non. Lorem ipsum dolor sit amet, con-sectetur adipiscing elit.</p>
</section>
<section class="footer-col" style="left:573px;width:224px">
  <h2>Our Blog</h2>
  <p class="blog-entry">Lorem ipsum dolor sit amet, consectetur adipiscing elit. Nam eget magna non.<br>Oct 25, 2010</p>
  <p class="blog-entry">Lorem ipsum dolor sit amet, consectetur adipiscing elit. Nam eget magna non.<br>Oct 25, 2010</p>
  <p class="blog-entry">Lorem ipsum dolor sit amet, consectetur adipiscing elit. Nam eget magna non.<br>Oct 25, 2010</p>
</section>

<footer class="bottom-bar">
  <nav class="bottom-nav"><a href="#">home</a><span>/</span><a href="#">apps</a><span>/</span><a href="#">support</a><span>/</span><a href="#">blog</a><span>/</span><a href="#">contact</a><span>/</span><a href="#">about</a></nav>
  <div class="bottom-brand">plumweave</div>
  <div class="copyright">copyright©2010. All rights reserver.</div>
</footer>
</body>
</html>
```